A small electrical company designed a vehicle wrap for the Corvan Haulmark 360

We designed a vehicle wrap for a small Los Angeles electrical company specializing in electrical repairs, air conditioning repair and installation, electric vehicle charging station installation, and electrical upgrades. Our clientele primarily serves residential and commercial customers. To stay within our budget, we chose a clear, eye-catching electrical and air conditioning logo that combined fonts and graphics to create a memorable impression.
Target Market(s)
electrical repair & installation, cooling&heating ,EV charger installation
Industry/Entity Type
electrical and Air conditioning
Requirements
Must have
- phone number:(555)4820173 Lic#:2048736 website www.quorvelectric.example
Nice to have
- my vehicle is Corvan haulmark 360 high roof 148'WB cargo van

```html
<!DOCTYPE html>
<html lang="en">
<head>
<meta charset="utf-8">
<title>Quorv Electric Solution Inc — Van Wrap</title>
<link rel="stylesheet" href="https://fonts.googleapis.com/css2?family=Oswald:wght@600&family=Montserrat:wght@700;800&family=Tinos&display=swap">
<style>
  :root {
    --orange: #e07b1a;
    --navy: #2b3442;
    --white: #ffffff;
    --trim: #1e2127;
    --glass: #3a4048;
    --tyre: #17191c;
    --rim: #c9ccd0;
    --lamp: #c8202a;
    --canvas: #eceef0;
  }
  html, body {
    margin: 0;
    padding: 0;
    width: 1200px;
    height: 2232px;
    overflow: hidden;
    background: var(--canvas);
  }
  .wrap-sheet { width: 1200px; height: 2232px; display: flex; flex-direction: column; }
  .view { display: block; width: 1200px; }
  .view-left, .view-right { height: 641px; }
  .view-rear { height: 950px; }
  .brand-name { font-family: "Oswald", sans-serif; font-weight: 600; fill: var(--navy); }
  .phone { font-family: "Montserrat", sans-serif; font-weight: 800; fill: var(--orange); }
  .site { font-family: "Montserrat", sans-serif; font-weight: 700; fill: var(--navy); }
  .licence { font-family: "Montserrat", sans-serif; font-weight: 700; fill: var(--navy); }
  .tagline { font-family: "Tinos", serif; fill: var(--white); }
  .mark-name { font-family: "Oswald", sans-serif; font-weight: 600; fill: var(--navy); }
  .service { font-family: "Montserrat", sans-serif; font-weight: 700; fill: var(--navy); }
  .rear-phone { font-family: "Montserrat", sans-serif; font-weight: 800; fill: var(--orange); }
  .rear-site { font-family: "Montserrat", sans-serif; font-weight: 700; fill: var(--white); }
</style>
</head>
<body>
<main class="wrap-sheet">

  <!-- Driver side -->
  <svg class="view view-left" viewBox="0 0 1200 641" xmlns="http://www.w3.org/2000/svg">
    <g class="van-body">
      <path fill="var(--white)" d="M40 470 L46 385 Q62 352 150 335 L245 230 Q275 205 335 200 L430 195 L432 115 Q440 103 470 102 L1148 106 Q1168 110 1170 140 L1174 480 Q1174 505 1148 505 L62 508 Q40 505 40 470 Z"/>
      <polygon fill="var(--orange)" points="948,106 1148,106 1168,125 1172,428 735,430 765,265"/>
      <polygon fill="var(--navy)" points="40,415 780,410 740,440 40,445"/>
      <path fill="var(--trim)" d="M40 445 L1174 432 L1174 480 Q1174 505 1148 505 L62 508 Q40 505 40 470 Z"/>
      <polygon fill="var(--orange)" points="650,482 760,482 790,470 690,470"/>
      <path fill="var(--glass)" d="M245 315 L258 248 Q272 225 330 222 L412 220 L412 320 Z"/>
      <rect x="1150" y="320" width="20" height="110" rx="6" fill="var(--lamp)"/>
      <circle cx="195" cy="518" r="72" fill="var(--tyre)"/><circle cx="195" cy="518" r="44" fill="var(--rim)"/>
      <circle cx="868" cy="515" r="72" fill="var(--tyre)"/><circle cx="868" cy="515" r="44" fill="var(--rim)"/>
    </g>
    <text class="licence" x="118" y="409" font-size="13">LIC# 2048736</text>
    <text class="brand-name" x="600" y="238" font-size="66" text-anchor="middle" textLength="275" lengthAdjust="spacingAndGlyphs">QUORV ELECTRIC</text>
    <text class="brand-name" x="600" y="305" font-size="66" text-anchor="middle" textLength="245" lengthAdjust="spacingAndGlyphs">SOLUTION INC</text>
    <text class="phone" x="605" y="360" font-size="34" text-anchor="middle">&#9990;555-482-0173</text>
    <text class="site" x="610" y="385" font-size="19" text-anchor="middle">QUORVELECTRIC.EXAMPLE</text>
    <g class="mark" aria-label="Quorv Electric name mark">
      <rect x="905" y="230" width="34" height="34" fill="var(--navy)"/>
      <text class="mark-name" x="950" y="266" font-size="52">QUORV</text>
    </g>
    <line x1="805" y1="388" x2="845" y2="388" stroke="var(--white)" stroke-width="2"/>
    <text class="tagline" x="983" y="394" font-size="27" text-anchor="middle">we power your homes</text>
    <line x1="1120" y1="388" x2="1150" y2="388" stroke="var(--white)" stroke-width="2"/>
  </svg>

  <!-- Passenger side -->
  <svg class="view view-right" viewBox="0 0 1200 641" xmlns="http://www.w3.org/2000/svg">
    <g class="van-body" transform="translate(1200 0) scale(-1 1)">
      <path fill="var(--white)" d="M40 470 L46 385 Q62 352 150 335 L245 230 Q275 205 335 200 L430 195 L432 115 Q440 103 470 102 L1148 106 Q1168 110 1170 140 L1174 480 Q1174 505 1148 505 L62 508 Q40 505 40 470 Z"/>
      <polygon fill="var(--orange)" points="948,106 1148,106 1168,125 1172,428 735,430 765,265"/>
      <polygon fill="var(--navy)" points="40,415 780,410 740,440 40,445"/>
      <path fill="var(--trim)" d="M40 445 L1174 432 L1174 480 Q1174 505 1148 505 L62 508 Q40 505 40 470 Z"/>
      <polygon fill="var(--orange)" points="650,482 760,482 790,470 690,470"/>
      <path fill="var(--glass)" d="M245 315 L258 248 Q272 225 330 222 L412 220 L412 320 Z"/>
      <rect x="1150" y="320" width="20" height="110" rx="6" fill="var(--lamp)"/>
      <circle cx="195" cy="518" r="72" fill="var(--tyre)"/><circle cx="195" cy="518" r="44" fill="var(--rim)"/>
      <circle cx="868" cy="515" r="72" fill="var(--tyre)"/><circle cx="868" cy="515" r="44" fill="var(--rim)"/>
    </g>
    <text class="licence" x="1010" y="409" font-size="13">LIC# 2048736</text>
    <text class="brand-name" x="600" y="238" font-size="66" text-anchor="middle" textLength="275" lengthAdjust="spacingAndGlyphs">QUORV ELECTRIC</text>
    <text class="brand-name" x="600" y="305" font-size="66" text-anchor="middle" textLength="245" lengthAdjust="spacingAndGlyphs">SOLUTION INC</text>
    <text class="phone" x="605" y="360" font-size="34" text-anchor="middle">&#9990;555-482-0173</text>
    <text class="site" x="610" y="385" font-size="19" text-anchor="middle">QUORVELECTRIC.EXAMPLE</text>
    <g class="mark" aria-label="Quorv Electric name mark">
      <rect x="92" y="230" width="34" height="34" fill="var(--navy)"/>
      <text class="mark-name" x="137" y="266" font-size="52">QUORV</text>
    </g>
    <line x1="55" y1="388" x2="85" y2="388" stroke="var(--white)" stroke-width="2"/>
    <text class="tagline" x="220" y="394" font-size="27" text-anchor="middle">we power your homes</text>
    <line x1="355" y1="388" x2="395" y2="388" stroke="var(--white)" stroke-width="2"/>
  </svg>

  <!-- Rear doors -->
  <svg class="view view-rear" viewBox="0 0 1200 950" xmlns="http://www.w3.org/2000/svg">
    <g class="van-rear">
      <path fill="var(--orange)" d="M300 120 Q310 70 380 62 L820 62 Q890 70 900 120 L960 520 L240 520 Z"/>
      <rect x="240" y="505" width="720" height="80" fill="var(--white)"/>
      <rect x="240" y="585" width="720" height="80" fill="var(--navy)"/>
      <path fill="var(--trim)" d="M245 665 L955 665 L960 860 Q960 880 940 880 L260 880 Q240 880 240 860 Z"/>
      <rect x="505" y="40" width="250" height="28" rx="10" fill="var(--trim)"/>
      <rect x="550" y="45" width="160" height="10" rx="4" fill="var(--lamp)"/>
      <line x1="625" y1="70" x2="625" y2="660" stroke="var(--trim)" stroke-width="2"/>
      <rect x="260" y="455" width="30" height="180" rx="10" fill="var(--lamp)"/>
      <rect x="960" y="455" width="30" height="180" rx="10" fill="var(--lamp)"/>
    </g>
    <text class="licence" x="818" y="187" font-size="14">LIC# 2048736</text>
    <g class="mark" aria-label="Quorv Electric name mark">
      <rect x="508" y="238" width="40" height="40" fill="var(--navy)"/>
      <text class="mark-name" x="562" y="281" font-size="62">QUORV</text>
    </g>
    <text class="brand-name" x="637" y="448" font-size="78" text-anchor="middle" textLength="565" lengthAdjust="spacingAndGlyphs">QUORV ELECTRIC SOLUTION INC</text>
    <line x1="352" y1="491" x2="428" y2="491" stroke="var(--white)" stroke-width="2.5"/>
    <text class="tagline" x="640" y="500" font-size="38" text-anchor="middle">we power your homes</text>
    <line x1="830" y1="491" x2="905" y2="491" stroke="var(--white)" stroke-width="2.5"/>
    <g class="service-list">
      <circle cx="340" cy="534" r="4.5" fill="var(--orange)"/>
      <text class="service" x="351" y="539" font-size="15.5">RESIDENTIAL &amp; COMMERCIAL</text>
      <text class="service" x="381" y="558" font-size="15.5">ELECTRICAL SERVICES</text>
      <circle cx="355" cy="572" r="4.5" fill="var(--orange)"/>
      <text class="service" x="365" y="577" font-size="15.5">ELECTRICAL INSPECTIONS</text>
      <circle cx="686" cy="537" r="4.5" fill="var(--orange)"/>
      <text class="service" x="698" y="542" font-size="15.5">EMERGENCY SERVICES</text>
      <circle cx="661" cy="556" r="4.5" fill="var(--orange)"/>
      <text class="service" x="675" y="561" font-size="15.5">EV CHARGER INSTALLATION</text>
      <circle cx="680" cy="575" r="4.5" fill="var(--orange)"/>
      <text class="service" x="693" y="580" font-size="15.5">SERVICE UPGRADATION</text>
    </g>
    <text class="rear-phone" x="455" y="631" font-size="40" text-anchor="middle">555-482-0173</text>
    <text class="rear-site" x="786" y="626" font-size="22" text-anchor="middle">QUORVELECTRIC.EXAMPLE</text>
  </svg>

</main>
</body>
</html>
```